Creative, Innovative PowerPoint Sales Deck Refresh needed

We are a technology firm in the Dallas, TX area and we need the powerpoint presentation used for our sales calls refreshed. This presentation is used in one of the first meetings we have with potential clients, so we want to make a memorable and positive impact - we want something that sets us apart from everyone else. We need 8 master slide templates created for our sales deck and a series of slides within the example sales deck need to be completely refreshed (slides 31-37 and 43 in the sample ppt file) We want a sales deck that is modern, innovative, creative, memorable and whimsical - NOT a typical boring "business" design. Colors should match or compliment the colors used in our logo. The logo in the footer of the attached sample ppt is old - it should be replaced with the newer logo attached. Please take a look at our website to get an idea of our culture and aesthetic www.brightkollow.com
Updates

Project Deadline Extended
Reason: We have received several designs we like and we want our entire team to have time to give them full consideration before making a decision.

Target Market(s)

Business executives

Industry/Entity Type

Information Technology

Font styles to use
Sans Serif

Requirements
Must have
• Our logo and LedgerPeak logo in footer
• Master Slide Templates
• Rework / redesign of slides 31-37 and 43
Nice to have
• We use Raleway font in a lot of our materials

```html
<!DOCTYPE html>
<html lang="en">
<head>
<meta charset="utf-8">
<title>brightkollow – Sales Deck Slides</title>
<link href="https://fonts.googleapis.com/css2?family=Raleway:wght@400;600;700;800&family=Open+Sans:wght@400;600;700&display=swap" rel="stylesheet">
<style>
:root{
  --canvas:#e4e4e4;
  --slide:#f4f4f4;
  --white:#ffffff;
  --ink:#1b1b1b;
  --grey:#7a7a7a;
  --line:#d8d8d8;
  --navy:#1c3f7a;
  --blue:#1f63ad;
  --sky:#5b9bd5;
  --pale:#8fb4dc;
  --orange:#f26a2e;
  --peach:#f4a07d;
  --slate:#8794b6;
  --charcoal:#5f5f5f;
}
*{box-sizing:border-box;margin:0;padding:0}
html,body{width:1200px;height:857px;overflow:hidden;background:var(--canvas)}
body{font-family:"Open Sans",sans-serif;color:var(--ink)}
.deck{display:grid;grid-template-columns:repeat(4,292px);grid-template-rows:repeat(5,164px);column-gap:3px;row-gap:5px;padding:7px 0 0 11px}
.slide{position:relative;background:var(--slide);overflow:hidden;box-shadow:0 1px 2px rgba(0,0,0,.25)}
.tab{position:absolute;top:0;left:50%;transform:translateX(-50%);display:flex;gap:1px}
.tab i{display:block;width:6px;height:4px;background:var(--ink)}
.tab i:nth-child(2){background:var(--blue)}.tab i:nth-child(3){background:var(--pale)}
.title{position:absolute;top:6px;left:0;right:0;text-align:center;font-family:Raleway,sans-serif;font-weight:700;font-size:8.5px}
.sub{position:absolute;top:16px;left:0;right:0;text-align:center;font-size:4.4px;color:var(--orange)}
.foot{position:absolute;left:0;right:0;bottom:0;height:10px;background:var(--white);border-top:1px solid var(--line);display:flex;align-items:center;padding:0 5px;font-size:3.6px;color:var(--grey)}
.brand{display:flex;align-items:center;gap:2px;font-family:Raleway,sans-serif;font-weight:700;font-size:4.4px;color:var(--ink)}
.brand b{width:5px;height:5px;border-radius:50%;background:var(--blue)}
.pg{margin-left:40px;color:var(--orange)}
.lp{margin-left:auto;font-family:Raleway,sans-serif;font-weight:800;font-size:4.6px;color:var(--ink);display:flex;align-items:center;gap:2px}
.lp b{width:4px;height:4px;background:var(--navy)}
.abs{position:absolute}
.bul{list-style:none;font-size:5.4px;line-height:8px}
.bul li::before{content:"▸ ";font-size:4px}
.chk{list-style:none;font-size:4.2px;line-height:6.2px;color:var(--orange);padding-left:6px}
.chk li::before{content:"✓ ";color:var(--blue)}
.tiny{font-size:3.3px;line-height:4.6px;color:var(--grey)}
.photo{position:absolute;border-radius:2px}
.stripes{position:absolute;display:flex;gap:2px}
.stripes i{display:block;width:6px;background:var(--ink)}
.stripes i:nth-child(2){background:var(--blue)}.stripes i:nth-child(3){background:var(--pale)}
.bigtitle{position:absolute;font-family:Raleway,sans-serif;font-weight:700;color:var(--ink)}
.band{position:absolute;left:0;right:0;top:62px;height:10px;background:var(--white);display:flex;align-items:center;font-size:4.6px}
.band .edge{width:40px;height:100%;background:var(--slate)}
.cols3{position:absolute;top:76px;left:46px;right:30px;display:flex;gap:10px}
.cols3 ul{flex:1;list-style:none;font-size:3.5px;line-height:5.5px}
.cols3 li::before{content:"• ";color:var(--orange)}
.cards{position:absolute;left:6px;right:6px;top:56px;display:flex;gap:3px}
.card{flex:1;height:48px;background:var(--white);display:flex;flex-direction:column;align-items:center;justify-content:center;gap:4px;text-align:center;font-size:3.4px;color:var(--orange);padding:0 2px}
.card svg{width:12px;height:12px}
.ico{fill:var(--charcoal)}
.flow{position:absolute;top:66px;left:12px;right:8px;display:flex;align-items:center;gap:4px}
.flow .box{width:52px;height:28px;background:var(--white);display:flex;align-items:center;justify-content:center;text-align:center;font-size:3.8px;color:var(--navy);padding:2px}
.arr{width:0;height:0;border-left:8px solid var(--slate);border-top:5px solid transparent;border-bottom:5px solid transparent}
.role{position:absolute;width:90px}
.role h4{font-size:4px;color:var(--blue);font-weight:700;margin-bottom:2px;padding-left:12px}
.role .dot{position:absolute;left:0;top:0;width:9px;height:9px;border-radius:50%;background:var(--sky)}
.role ul{list-style:none;padding-left:12px}
.role li::before{content:"• ";color:var(--orange)}
.chev{position:absolute;top:50px;left:26px;display:flex}
.chev div{width:50px;height:20px;margin-right:-4px;clip-path:polygon(0 0,88% 0,100% 50%,88% 100%,0 100%,12% 50%);display:flex;align-items:flex-end;justify-content:center;padding-bottom:2px;font-size:3px;color:var(--white)}
.gp{position:absolute;top:40px;left:10px;right:16px;list-style:none;font-size:3.9px;line-height:5px}
.gp li{position:relative;padding-left:15px;margin-bottom:4.4px}
.gp li::before{content:"✓";position:absolute;left:2px;color:var(--orange);font-size:6px}
.gp b{color:var(--navy)}
.risk{position:absolute;left:18px;right:18px;top:40px;display:grid;grid-template-columns:repeat(5,1fr);grid-template-rows:40px 40px;background:var(--white)}
.risk div{border:0.5px solid var(--line);display:flex;flex-direction:column;align-items:center;justify-content:center;gap:3px;text-align:center;font-size:3.2px;color:var(--grey);padding:0 2px}
.risk span{width:7px;height:7px;background:var(--charcoal);border-radius:1px;opacity:.6}
</style>
</head>
<body>
<main class="deck">

<!-- 1 Methodology -->
<section class="slide" style="background:var(--white)">
  <div class="stripes" style="left:142px;top:0;height:52px"><i></i><i></i><i></i></div>
  <div class="brand abs" style="left:142px;top:64px"><b></b>brightkollow</div>
  <div class="bigtitle" style="left:142px;top:82px;font-size:12px">Methodology</div>
  <div class="stripes" style="left:142px;top:118px;height:46px"><i></i><i></i><i></i></div>
</section>

<!-- 2 Project Theme -->
<section class="slide">
  <div class="tab"><i></i><i></i><i></i></div>
  <div class="title">Project Theme</div>
  <svg class="abs" style="left:40px;top:30px" width="150" height="120" viewBox="0 0 150 120">
    <g fill="none" stroke="#f26a2e" stroke-width=".6" stroke-dasharray="2 1.5">
      <rect x="6" y="4" width="100" height="30"/><rect x="6" y="42" width="100" height="34"/><rect x="6" y="84" width="100" height="34"/>
    </g>
    <g fill="#1c3f7a"><circle cx="6" cy="4" r="4"/><circle cx="6" cy="42" r="4"/><circle cx="6" cy="84" r="4"/></g>
    <g fill="#fff" font-size="3" text-anchor="middle" font-family="Open Sans"><text x="6" y="5">01</text><text x="6" y="43">02</text><text x="6" y="85">03</text></g>
    <g fill="#1c3f7a" font-size="5" font-weight="700" font-family="Open Sans"><text x="14" y="11">Simple</text><text x="14" y="50">Comprehensive</text><text x="14" y="92">Long Term</text></g>
    <g fill="#7a7a7a" font-size="3" font-family="Open Sans">
      <text x="18" y="18">✓ One source of truth</text><text x="18" y="23">✓ Integration of key practices</text><text x="18" y="28">✓ Automate your processes</text>
      <text x="18" y="57">✓ Fully integrated enterprise system</text><text x="18" y="62">✓ Everything you need now and later</text><text x="18" y="67">✓ Flexibility to evolve as you change</text><text x="18" y="72">✓ Product is proven with a clear future</text>
      <text x="18" y="99">✓ Lowest risk</text><text x="18" y="104">✓ Streamlined IT staff to maintain</text><text x="18" y="109">✓ The last solution you will need</text>
    </g>
    <polygon points="114,46 120,60 114,74" fill="#f26a2e"/>
  </svg>
  <div class="abs" style="left:172px;top:66px;display:flex;flex-direction:column;gap:4px">
    <div style="width:70px;height:16px;background:var(--blue);color:#fff;font-size:3.2px;text-align:center;padding-top:4px;border-radius:1px">LedgerPeak provides real time visibility for your team</div>
    <div style="width:70px;height:16px;background:var(--blue);color:#fff;font-size:3.2px;text-align:center;padding-top:4px;border-radius:1px">LedgerPeak is right-sized for Able Tape</div>
    <div style="width:70px;height:16px;background:var(--blue);color:#fff;font-size:3.2px;text-align:center;padding-top:4px;border-radius:1px">LedgerPeak is the enduring and safe choice</div>
  </div>
  <footer class="foot"><span class="brand"><b></b>brightkollow</span><span class="pg">26 · © brightkollow</span><span class="lp"><b></b>LEDGERPEAK</span></footer>
</section>

<!-- 3 Venlo -->
<section class="slide">
  <div class="tab"><i></i><i></i><i></i></div>
  <div class="title">Venlo</div>
  <div class="abs" style="right:8px;top:5px;font-family:Raleway,sans-serif;font-weight:700;font-size:7px;color:var(--blue)">Venlo</div>
  <div class="abs" style="left:18px;top:34px">
    <ul class="bul"><li>Electronics manufacturer</li><li>Set top boxes for hospitality industry</li><li>Experiencing rapid growth</li><li>5 month implementation</li><li>LedgerPeak Footprint</li></ul>
    <ul class="chk"><li>CRM</li><li>Financials</li><li>Manufacturing</li><li>Order Entry</li><li>Project Management</li><li>Procurement</li><li>Demand Planning</li></ul>
  </div>
  <div class="photo" role="img" aria-label="Photo of a hand holding a remote in front of a hotel television" style="left:152px;top:48px;width:122px;height:70px;background:linear-gradient(135deg,#a9c3c8,#7b999c);border:2px solid #fff"></div>
  <footer class="foot"><span class="brand"><b></b>brightkollow</span><span class="pg">27 · © brightkollow</span><span class="lp"><b></b>LEDGERPEAK</span></footer>
</section>

<!-- 4 Orvane -->
<section class="slide">
  <div class="tab"><i></i><i></i><i></i></div>
  <div class="title">Orvane Therapeutics</div>
  <div class="abs" style="right:8px;top:5px;font-family:Raleway,sans-serif;font-weight:700;font-size:7px;color:var(--orange)">orvane</div>
  <div class="abs" style="left:18px;top:36px">
    <ul class="bul"><li>Baltimore area Biomedical company</li><li>Platelet and plasma therapy system</li><li>Phased 6 month implementation</li><li>LedgerPeak Footprint:</li></ul>
    <ul class="chk"><li>Financials</li><li>Order Entry</li><li>Manufacturing</li><li>Procurement</li><li>CRM</li></ul>
  </div>
  <div class="photo" role="img" aria-label="Product photo of a black Clarex medical device" style="left:172px;top:52px;width:72px;height:64px;background:radial-gradient(circle at 50% 40%,#4a4a4a,#1e1e1e);border-radius:8px"></div>
  <footer class="foot"><span class="brand"><b></b>brightkollow</span><span class="pg">28 · © brightkollow</span><span class="lp"><b></b>LEDGERPEAK</span></footer>
</section>

<!-- 5 Project Scope -->
<section class="slide">
  <div class="tab"><i></i><i></i><i></i></div>
  <div class="title">Project Scope</div>
  <div class="sub" style="top:15px;color:var(--grey)">Turnkey solution for all of your <span style="color:var(--orange)">business needs</span></div>
  <div class="band"><span class="edge"></span><span style="flex:1;padding-left:30px">● Technology</span><span style="flex:1">● People</span><span style="flex:1">● Process</span><span class="edge"></span></div>
  <div class="cols3">
    <ul><li>Accounting</li><li>Order Entry &amp; Fulfillment</li><li>Scheduling</li><li>Manufacturing</li><li>WMS</li></ul>
    <ul><li>Business Scenario Testing</li><li>End-to-End Training</li><li>Change Management</li></ul>
    <ul><li>Formal and Proven Methodology</li><li>Gate Reviews and Status Checks</li><li>Formal Signoffs</li></ul>
  </div>
  <footer class="foot"><span class="brand"><b></b>brightkollow</span><span class="pg">29 · © brightkollow</span><span class="lp"><b></b>LEDGERPEAK</span></footer>
</section>

<!-- 6 Project Benefits -->
<section class="slide">
  <div class="tab"><i></i><i></i><i></i></div>
  <div class="title">Project Benefits</div>
  <div class="band"><span class="edge" style="width:26px"></span><span style="flex:1;padding-left:12px">● Integrated Environment</span><span style="flex:.8">● Improved Efficiency</span><span style="flex:1.1">● Improved Operating Performance</span><span class="edge" style="width:20px"></span></div>
  <div class="cols3" style="left:30px;right:20px">
    <ul><li>Flexible system that is easy to maintain</li><li>Eliminate duplication and errors</li><li>Drive Consistency</li><li>Simplify Transactional Flow</li></ul>
    <ul style="flex:.6"><li>Process automation</li><li>Eliminate work-arounds</li></ul>
    <ul><li>Operations effectiveness with better, faster information</li><li>Understand and control cost through visibility and reporting</li><li>Improved data accuracy and accessibility</li><li>Simplify</li></ul>
  </div>
  <footer class="foot"><span class="brand"><b></b>brightkollow</span><span class="pg">30 · © brightkollow</span><span class="lp"><b></b>LEDGERPEAK</span></footer>
</section>

<!-- 7 Roles -->
<section class="slide">
  <div class="tab"><i></i><i></i><i></i></div>
  <div class="title">Roles &amp; Responsibilities</div>
  <div class="role tiny" style="left:12px;top:30px"><span class="dot"></span><h4>PROJECT SPONSOR</h4><ul><li>Overall project champion</li><li>Responsible for ensuring deliverables</li><li>Monitor results and performance</li><li>Provide necessary facilities</li></ul></div>
  <div class="role tiny" style="left:105px;top:30px"><span class="dot"></span><h4>QUALITY ASSURANCE</h4><ul><li>Responsible for quality work</li><li>Provide expertise and direction</li><li>Monitor and support the team</li><li>Implement and manage go-live</li></ul></div>
  <div class="role tiny" style="left:196px;top:30px"><span class="dot"></span><h4>CHANGE MANAGEMENT</h4><ul><li>Responsible for enabling transition</li><li>Assess the impact of changes</li><li>Assist in executing communication</li><li>Develop and deliver training</li></ul></div>
  <div class="role tiny" style="left:12px;top:92px"><span class="dot"></span><h4>STEERING COMMITTEE</h4><ul><li>Composed of key leadership</li><li>Sets overall project direction</li><li>Supports the vision of project</li><li>Bi-weekly status meetings</li><li>Strategic issue resolution</li></ul></div>
  <div class="role tiny" style="left:105px;top:92px"><span class="dot"></span><h4>PROJECT MANAGEMENT</h4><ul><li>Weekly project team meetings</li><li>Status reports to the committee</li><li>Ensure scope is on time and budget</li><li>Mitigate risks</li></ul></div>
  <div class="role tiny" style="left:196px;top:92px"><span class="dot"></span><h4>TEAM LEADERS/SUPERUSERS</h4><ul><li>Execute the project plan</li><li>Identify risks and integration</li><li>Configure and test systems</li><li>Design business processes</li><li>Weekly team status meetings</li></ul></div>
  <footer class="foot"><span class="brand"><b></b>brightkollow</span><span class="pg">31 · © brightkollow</span><span class="lp"><b></b>LEDGERPEAK</span></footer>
</section>

<!-- 8 Phase One overview -->
<section class="slide">
  <div class="tab"><i></i><i></i><i></i></div>
  <div class="title">Phase One Methodology</div>
  <div class="chev">
    <div style="background:var(--ink);clip-path:polygon(0 0,88% 0,100% 50%,88% 100%,0 100%)">Project Initiation</div>
    <div style="background:var(--navy)">Solution Design</div>
    <div style="background:var(--slate)">Application Configuration</div>
    <div style="background:var(--orange)">Testing &amp; Preparation</div>
    <div style="background:var(--sky)">Deployment &amp; Support</div>
  </div>
  <div class="abs" style="top:104px;left:20px;right:20px;display:flex;justify-content:space-around;font-size:4.4px;color:var(--navy)">
    <span>CHANGE MANAGEMENT</span><span style="border-left:1px solid var(--ink);border-right:1px solid var(--ink);padding:0 14px">USER INVOLVEMENT</span><span>PROGRAM MANAGEMENT</span>
  </div>
  <footer class="foot"><span class="brand"><b></b>brightkollow</span><span class="pg">32 · © brightkollow</span><span class="lp"><b></b>LEDGERPEAK</span></footer>
</section>

<!-- 9 Project Initiation -->
<section class="slide">
  <div class="tab"><i></i><i></i><i></i></div>
  <div class="title">Phase One Methodology</div><div class="sub">Project Initiation</div>
  <div class="flow">
    <div class="box">Conduct Kickoff Meeting</div><span class="arr"></span>
    <div class="box">Finalize and Publish Project Schedule</div><span class="arr"></span>
    <div class="box">Requirements Definition and Design</div><span class="arr"></span>
    <div class="box">Requirements Traceability Matrix (RTM) Signoff</div>
  </div>
  <footer class="foot"><span class="brand"><b></b>brightkollow</span><span class="pg">33 · © brightkollow</span><span class="lp"><b></b>LEDGERPEAK</span></footer>
</section>

<!-- 10 Solution Design -->
<section class="slide">
  <div class="tab"><i></i><i></i><i></i></div>
  <div class="title">Phase One Methodology</div><div class="sub">Solution Design</div>
  <div class="abs" style="left:42px;top:40px;width:207px;height:84px;background:var(--white);border:0.5px solid var(--line)"></div>
  <svg class="abs" style="left:33px;top:34px" width="26" height="26" viewBox="0 0 26 26"><circle cx="13" cy="13" r="13" fill="#f26a2e"/><circle cx="13" cy="11" r="4.5" fill="none" stroke="#fff" stroke-width="1.2"/><rect x="11" y="16" width="4" height="3" fill="#fff"/></svg>
  <ul class="bul abs" style="left:96px;top:52px;font-size:5.6px">
    <li>Map and Gap Against RTM</li><li>Identify Solutions for Gaps</li>
  </ul>
  <ul class="chk abs" style="left:100px;top:69px"><li>Custom Development</li><li>Phase Two Initiative</li><li>Business Process Change</li></ul>
  <ul class="bul abs" style="left:96px;top:91px;font-size:5.6px"><li>Business Flow Recommendation</li></ul>
  <footer class="foot"><span class="brand"><b></b>brightkollow</span><span class="pg">34 · © brightkollow</span><span class="lp"><b></b>LEDGERPEAK</span></footer>
</section>

<!-- 11 Application Configuration -->
<section class="slide">
  <div class="tab"><i></i><i></i><i></i></div>
  <div class="title">Phase One Methodology</div><div class="sub">Application Configuration</div>
  <div class="cards" style="top:56px">
    <div class="card"><svg viewBox="0 0 12 12"><path class="ico" d="M2 1l9 9-1 1-9-9zM10 1l1 1-9 9-1-1z"/></svg>System Setup</div>
    <div class="card"><svg viewBox="0 0 12 12"><path class="ico" d="M6 1l5 2.5-5 2.5-5-2.5zM1 6l5 2.5 5-2.5v1.5l-5 2.5-5-2.5z"/></svg>Extended Prototyping</div>
    <div class="card"><svg viewBox="0 0 12 12"><path d="M4 3L1 6l3 3M8 3l3 3-3 3M7 2L5 10" fill="none" stroke="#5f5f5f"/></svg>Develop Test Scripts</div>
    <div class="card" style="flex:1.4"><svg viewBox="0 0 12 12"><rect class="ico" x="1" y="2" width="10" height="2"/><rect class="ico" x="1" y="5" width="10" height="2"/><rect class="ico" x="1" y="8" width="10" height="2"/></svg>Initiate Data Cleansing &amp; Conversion Process</div>
  </div>
  <footer class="foot"><span class="brand"><b></b>brightkollow</span><span class="pg">35 · © brightkollow</span><span class="lp"><b></b>LEDGERPEAK</span></footer>
</section>

<!-- 12 Testing & Preparation -->
<section class="slide">
  <div class="tab"><i></i><i></i><i></i></div>
  <div class="title">Phase One Methodology</div><div class="sub">Testing &amp; Preparation</div>
  <div class="cards">
    <div class="card"><svg viewBox="0 0 12 12"><circle cx="6" cy="6" r="4.5" fill="none" stroke="#5f5f5f" stroke-width="1.2"/><circle class="ico" cx="6" cy="6" r="1.5"/></svg>Unit Testing – Individual Modules</div>
    <div class="card"><svg viewBox="0 0 12 12"><path d="M2 10l6-6M7 2a3 3 0 1 0 3 3" fill="none" stroke="#5f5f5f" stroke-width="1.4"/></svg>Integration Testing – End to End</div>
    <div class="card"><svg viewBox="0 0 12 12"><circle class="ico" cx="6" cy="4" r="2.5"/><path class="ico" d="M1.5 11a4.5 4 0 0 1 9 0z"/></svg>User Acceptance Testing</div>
    <div class="card"><svg viewBox="0 0 12 12"><path d="M10 5a4 4 0 0 0-7.5-1M2 7a4 4 0 0 0 7.5 1" fill="none" stroke="#5f5f5f" stroke-width="1.3"/></svg>Full Life Cycle Simulations</div>
    <div class="card"><svg viewBox="0 0 12 12"><circle class="ico" cx="3.5" cy="4" r="1.8"/><circle class="ico" cx="8.5" cy="4" r="1.8"/><path class="ico" d="M0.5 10a3 3 0 0 1 6 0zM5.5 10a3 3 0 0 1 6 0z"/></svg>End User Training</div>
  </div>
  <footer class="foot"><span class="brand"><b></b>brightkollow</span><span class="pg">36 · © brightkollow</span><span class="lp"><b></b>LEDGERPEAK</span></footer>
</section>

<!-- 13 Deployment & Support -->
<section class="slide">
  <div class="tab"><i></i><i></i><i></i></div>
  <div class="title">Phase One Methodology</div><div class="sub">Deployment &amp; Support</div>
  <div class="cards" style="top:54px">
    <div class="card"><svg viewBox="0 0 12 12"><circle cx="6" cy="6" r="3.5" fill="none" stroke="#1c3f7a" stroke-width="2" stroke-dasharray="1.6 1"/></svg>Setup Production Environment</div>
    <div class="card"><svg viewBox="0 0 12 12"><ellipse cx="6" cy="3" rx="4.5" ry="1.6" fill="#1c3f7a"/><rect x="1.5" y="4" width="9" height="2.4" fill="#1c3f7a"/><rect x="1.5" y="7.4" width="9" height="2.4" fill="#1c3f7a"/></svg>Convert Live Data</div>
    <div class="card"><svg viewBox="0 0 12 12"><path d="M11 1L1 5.5l4 1.5 1.5 4z" fill="#1c3f7a"/></svg>GO LIVE!</div>
    <div class="card"><svg viewBox="0 0 12 12"><path d="M1 2h10v6H5l-3 2.5V8H1z" fill="#1c3f7a"/></svg>Post Go-Live Support</div>
    <div class="card"><svg viewBox="0 0 12 12"><path d="M1 5h2.5v6H1zM4.5 5L7 1.5c1 0 1.5.5 1.2 2L8 5h3l-1 6H4.5z" fill="#1c3f7a"/></svg>Project Closeout</div>
  </div>
  <footer class="foot"><span class="brand"><b></b>brightkollow</span><span class="pg">37 · © brightkollow</span><span class="lp"><b></b>LEDGERPEAK</span></footer>
</section>

<!-- 14 Gate Reviews -->
<section class="slide">
  <div class="tab"><i></i><i></i><i></i></div>
  <div class="title">Gate Reviews &amp; Signoffs</div>
  <div class="abs" style="left:0;right:0;top:30px;height:4px;background:#e9e9e9"></div>
  <div class="abs" style="left:0;right:0;top:51px;text-align:center;font-size:3.4px">PHASE</div>
  <div class="abs" style="left:8px;right:8px;top:59px;display:grid;grid-template-columns:repeat(7,1fr);text-align:center;font-size:3.1px;color:var(--grey)">
    <div><svg width="8" height="8"><path d="M1 1l6 3-6 3z" fill="#777"/></svg><br><span style="color:var(--orange)">Project Kickoff</span></div>
    <div><svg width="8" height="8"><path d="M1 1h6M1 4h6M1 7h6" stroke="#777"/></svg><br>Project Initiation</div>
    <div><svg width="8" height="8"><rect x="1" y="1" width="6" height="6" fill="none" stroke="#777"/></svg><br>Unit Testing</div>
    <div><svg width="8" height="8"><path d="M1 7l6-6" stroke="#777" stroke-width="1.5"/></svg><br>Integration Testing</div>
    <div><svg width="8" height="8"><circle cx="4" cy="3" r="2" fill="#777"/><path d="M0 8a4 3 0 0 1 8 0z" fill="#777"/></svg><br><b style="color:var(--ink)">UAT</b></div>
    <div><svg width="8" height="8"><path d="M7 1L1 4l3 1 1 3z" fill="#777"/></svg><br>Deployment</div>
    <div><svg width="8" height="8"><rect x="1" y="3" width="6" height="4" fill="#777"/></svg><br>Project Closeout</div>
  </div>
  <div class="abs" style="left:0;right:0;top:78px;text-align:center;font-size:3.6px;font-weight:700;border-bottom:0.5px solid var(--line);padding-bottom:1px">ACCEPTANCE REQUIRED</div>
  <div class="abs" style="left:8px;right:8px;top:86px;display:grid;grid-template-columns:repeat(7,1fr);gap:2px;font-size:2.9px;line-height:4px;color:var(--grey)">
    <div style="color:var(--orange)">Statement of work is signed and approved</div><div>Requirements matrix is signed off as complete</div><div>Unit testing is completed and signed off</div><div>Integration testing is complete and signed off</div><div>User acceptance testing is signed off</div><div>System acceptance certificate signed off</div><div>Project closeout certificate is signed off</div>
  </div>
  <footer class="foot"><span class="brand"><b></b>brightkollow</span><span class="pg">38 · © brightkollow</span><span class="lp"><b></b>LEDGERPEAK</span></footer>
</section>

<!-- 15 Organizational Change -->
<section class="slide" style="background:var(--white)">
  <div class="stripes" style="left:138px;top:0;height:48px"><i></i><i></i><i></i></div>
  <div class="brand abs" style="left:138px;top:60px"><b></b>brightkollow</div>
  <div class="bigtitle" style="left:136px;top:78px;font-size:12.5px;line-height:15px">Organizational<br>Change</div>
  <div class="stripes" style="left:138px;top:116px;height:48px"><i></i><i></i><i></i></div>
</section>

<!-- 16 Change Management -->
<section class="slide">
  <div class="tab"><i></i><i></i><i></i></div>
  <div class="title">Change Management</div>
  <div class="sub" style="top:15px;color:var(--grey)">Change Curve · <span style="color:var(--orange)">How People Respond to Change</span></div>
  <p class="abs tiny" style="left:8px;top:74px;width:82px;text-align:right;font-style:italic">There is a predictable drop-off in performance due to new processes and systems. A targeted plan can be achieved by proactively managing the change.</p>
  <svg class="abs" style="left:94px;top:36px;background:#fff;border:0.5px solid #ccc" width="188" height="106" viewBox="0 0 188 106">
    <polyline fill="none" stroke="#1f63ad" stroke-width="1" points="10,36 30,44 50,58 62,70 72,80 78,76 84,92 90,74 96,86 102,80 110,90 118,66 126,72 134,54 146,46 164,24 176,12"/>
    <g font-size="3.4" fill="#f26a2e" font-family="Open Sans">
      <text x="12" y="32">Uninformed Optimism</text><text x="26" y="54">Immobilization and Denial</text><text x="54" y="66">Anger</text><text x="52" y="76">Bargaining</text><text x="44" y="88">Informed Pessimism</text><text x="84" y="100">Despair</text><text x="102" y="86">Testing</text><text x="112" y="74">Hopeful Realism</text><text x="124" y="62">Acceptance</text><text x="136" y="44">Informed Optimism</text><text x="142" y="32">Initiative Completion</text><text x="146" y="14">Continuous Improvement</text>
    </g>
  </svg>
  <footer class="foot"><span class="brand"><b></b>brightkollow</span><span class="pg">40 · © brightkollow</span><span class="lp"><b></b>LEDGERPEAK</span></footer>
</section>

<!-- 17 Guiding Principles -->
<section class="slide">
  <div class="tab"><i></i><i></i><i></i></div>
  <div class="title">Guiding Principles</div>
  <ul class="gp">
    <li><b>Take Ownership</b> take initiative and don't pass the buck if you could easily resolve an issue or help a team member.</li>
    <li><b>Stay Flexible</b> be willing to try things differently; anticipate and be open to change. Keep smiling and <span style="color:var(--orange)">maintain a positive attitude.</span></li>
    <li><b>Apply "SPF"</b> whenever possible, strive for simplification, purification and focus on standard functionality.</li>
    <li><b>Think Big Picture</b> think how your work affects everyone in your department and the company.</li>
    <li><b>Act as a Team</b> teamwork is crucial; we achieve more as a team than we ever can alone.</li>
    <li><b>Maintain Open Communication</b> continuous, two way communication is crucial; provide honest feedback.</li>
    <li><b>Identify Solutions</b> be proactive in looking for answers; seek out resolution of obstacles.</li>
  </ul>
  <footer class="foot"><span class="brand"><b></b>brightkollow</span><span class="pg">41 · © brightkollow</span><span class="lp"><b></b>LEDGERPEAK</span></footer>
</section>

<!-- 18 Project Risks -->
<section class="slide">
  <div class="tab"><i></i><i></i><i></i></div>
  <div class="title">Project Risks</div>
  <div class="risk">
    <div><span></span>Scope creep</div><div><span></span>Delayed decision-making</div><div><span></span>Lack of executive leadership</div><div><span></span>Conversely, leadership chaos</div><div><span></span>People affected by change have little input</div>
    <div><span></span>Lack of critical skills</div><div><span></span>Retention and morale problems</div><div><span></span>Simultaneous, multiple initiatives</div><div><span></span>Interruptions of day-to-day operations</div><div><span></span>Overly customizing to fit existing silos</div>
  </div>
  <footer class="foot"><span class="brand"><b></b>brightkollow</span><span class="pg">42 · © brightkollow</span><span class="lp"><b></b>LEDGERPEAK</span></footer>
</section>

<!-- 19 Five Key Areas -->
<section class="slide">
  <div class="tab"><i></i><i></i><i></i></div>
  <div class="title">Five Key Areas of User Adoption</div>
  <svg class="abs" style="left:8px;top:42px" width="276" height="86" viewBox="0 0 276 86">
    <g opacity=".95"><circle cx="40" cy="42" r="32" fill="#5f5f5f"/><circle cx="91" cy="42" r="32" fill="#8794b6"/><circle cx="142" cy="42" r="32" fill="#6fa9d8"/><circle cx="193" cy="42" r="32" fill="#f4a07d"/><circle cx="244" cy="42" r="32" fill="#9aa6c6"/></g>
    <g fill="#fff" font-size="4" font-weight="700" text-anchor="middle" font-family="Open Sans">
      <rect x="35" y="30" width="10" height="2"/><rect x="35" y="34" width="10" height="2"/><text x="40" y="52">Alignment</text>
      <path d="M86 30h10v6h-5l-3 2v-2h-2z"/><text x="91" y="52">Communication</text>
      <rect x="138" y="29" width="8" height="9"/><text x="142" y="52">Training</text>
      <circle cx="193" cy="34" r="4"/><text x="193" y="52">Support</text>
      <path d="M239 38a5 5 0 0 1 10 0" fill="none" stroke="#fff" stroke-width="1.4"/><text x="244" y="52">Measurement</text>
    </g>
  </svg>
  <footer class="foot"><span class="brand"><b></b>brightkollow</span><span class="pg">43 · © brightkollow</span><span class="lp"><b></b>LEDGERPEAK</span></footer>
</section>

<!-- 20 Steps to Adoption -->
<section class="slide">
  <div class="tab"><i></i><i></i><i></i></div>
  <div class="title">Steps to Adoption</div>
  <svg class="abs" style="left:14px;top:30px" width="150" height="118" viewBox="0 0 150 118">
    <g fill="none" stroke-width="3">
      <path d="M62 14a46 46 0 0 1 30 0" stroke="#1c3f7a"/><path d="M112 30a46 46 0 0 1 8 36" stroke="#1c3f7a"/>
      <path d="M116 82a46 46 0 0 1-22 24" stroke="#1f63ad"/><path d="M84 110a46 46 0 0 1-24-2" stroke="#8fb4dc"/>
      <path d="M38 92a46 46 0 0 1-6-34" stroke="#b7bfd8"/><path d="M36 42a46 46 0 0 1 16-22" stroke="#8794b6"/>
    </g>
    <g font-size="3.6" fill="#1b1b1b" font-family="Open Sans">
      <text x="30" y="6">Establish</text><text x="30" y="10">On-Going</text><text x="30" y="14">Performance</text><text x="30" y="18">Criteria</text>
      <text x="98" y="6">Develop</text><text x="98" y="10">Go-Live</text><text x="98" y="14">Success</text><text x="98" y="18">Criteria</text>
      <text x="122" y="50">Conduct</text><text x="122" y="54">User</text><text x="122" y="58">Acceptance</text><text x="122" y="62">Testing</text>
      <text x="96" y="94">Develop</text><text x="96" y="98">Go-Live</text><text x="96" y="102">Training</text><text x="96" y="106">Support Plan</text>
      <text x="44" y="104">Conduct</text><text x="44" y="108">End User</text><text x="44" y="112">Training</text>
      <text x="4" y="54">Develop</text><text x="4" y="58">Continuing</text><text x="4" y="62">Education</text><text x="4" y="66">Plan</text>
    </g>
  </svg>
  <p class="abs tiny" style="left:176px;top:72px;width:100px;font-size:3.5px">Review success criteria 30 days after Go-Live<br>Document and communicate performance expectations</p>
  <footer class="foot"><span class="brand"><b></b>brightkollow</span><span class="pg">44 · © brightkollow</span><span class="lp"><b></b>LEDGERPEAK</span></footer>
</section>

</main>
</body>
</html>
```